Core Values - Poster

Develop a poster to display core values int he company. The design has to be align to the character and feel of the company. See our website for some inspiration. The Core Values are also listed on our website.
Our 4 core values are:
Excellence
We deliver quality services of unmatched value, constantly raising the bar on our performance, through a commitment to excellence, innovation, teamwork, ongoing learning, continuous improvement, an intense focus on client needs, and a dedication to meet those needs with a sense of urgency.
Integrity
We demonstrate honesty, fairness, openness and clear boundaries in all our interactions, behaviours and practices within the organisation and with our clients, stakeholders and the wider community. We act in accordance with our values, even when it’s difficult. We adhere to the highest ethical standards as we strive to do what is right and fair for our clients and for each other.
Sincerity
We embrace human emotions and values, and believe that sincerity is a fundamental human behaviour. We are honest with our team, and with clients in the work we do, and the way we do it. We set high expectations for ourselves to motivate hard work, and we will offer clients something that has been crafted with care, consideration and with authenticity, without cutting corners. We will put people first, and will always genuinely care.
Humility
We believe in a flat hierarchy, and that every person within the organisation is a floor sweeper. We’re not always right — we don’t have all the answers — and we know it. We’re all humans after all, and we’re not afraid to ask for help. We encourage everyone to Be Yourself, Be Open, Stay Hungry and Humble, Collaborate, Challenge, Decide and Just Do.
Everything in our Core Values need to be on the poster, which will be large (minimum 4x A4 size).
Our logo is attached in this brief - there are several colour options and layouts. Logo should be include in the poster.

```html
<!DOCTYPE html>
<html lang="en">
<head>
<meta charset="utf-8">
<title>Core Values – The Mindwell Company</title>
<link href="https://fonts.googleapis.com/css2?family=Arvo:wght@700&family=Raleway:wght@400;500;700&display=swap" rel="stylesheet">
<style>
  :root {
    --sand: #e4ddd3;
    --paper: #ffffff;
    --leaf: #7dc142;
    --olive: #3b3a1c;
    --ink: #2b2b1d;
    --ghost: #f1efec;
  }
  * { margin: 0; padding: 0; box-sizing: border-box; }
  html, body { width: 849px; height: 1200px; overflow: hidden; background: var(--paper); }
  .poster {
    position: relative;
    width: 849px;
    height: 1200px;
    background: var(--paper);
    font-family: "Raleway", sans-serif;
    color: var(--ink);
    overflow: hidden;
  }
  .masthead {
    position: absolute; left: 0; top: 0;
    width: 849px; height: 228px;
    background: var(--sand);
    display: flex; align-items: center; justify-content: center;
  }
  .brand {
    display: flex; align-items: center; gap: 18px;
    font-family: "Raleway", sans-serif;
    font-weight: 500;
    font-size: 54px;
    color: var(--ink);
    letter-spacing: 0.5px;
  }
  .brand-dot {
    width: 46px; height: 46px; border-radius: 50%;
    background: var(--leaf);
  }
  .footer {
    position: absolute; left: 0; top: 1140px;
    width: 849px; height: 60px;
    background: var(--sand);
    display: flex; align-items: center; justify-content: center;
    font-family: "Arvo", serif; font-weight: 700;
    font-size: 20px; letter-spacing: 2px;
    color: var(--olive);
  }
  .backdrop {
    position: absolute;
    background: var(--ghost);
  }
  .backdrop-award { left: 675px; top: 250px; width: 174px; height: 290px; border-radius: 87px 0 0 20px; }
  .backdrop-scales { left: 0; top: 430px; width: 185px; height: 230px; border-radius: 0 30px 30px 0; }
  .backdrop-hearts { left: 577px; top: 655px; width: 272px; height: 255px; border-radius: 120px 0 0 60px; }
  .backdrop-people { left: 0; top: 810px; width: 170px; height: 330px; border-radius: 0 85px 0 0; }
  .icon {
    position: absolute;
    background: var(--olive);
  }
  .icon-award { left: 142px; top: 274px; width: 120px; height: 160px; border-radius: 60px 60px 12px 12px; }
  .icon-scales { left: 122px; top: 486px; width: 160px; height: 110px; border-radius: 14px; }
  .icon-hearts { left: 130px; top: 730px; width: 145px; height: 120px; border-radius: 60px 60px 70px 70px; }
  .icon-people { left: 148px; top: 926px; width: 110px; height: 154px; border-radius: 50px 50px 8px 8px; }
  .value {
    position: absolute;
    width: 382px;
  }
  .value-title {
    display: inline-block;
    width: 178px; height: 38px;
    background: var(--leaf);
    font-family: "Arvo", serif; font-weight: 700;
    font-size: 24px; line-height: 38px;
    color: var(--olive);
    text-align: center;
    letter-spacing: 0.5px;
  }
  .value-text {
    margin-top: 22px;
    font-size: 12px;
    line-height: 14.8px;
    text-align: justify;
    letter-spacing: 0.6px;
    font-weight: 500;
  }
  .value-text strong { font-weight: 700; }
  .value-excellence { left: 342px; top: 279px; }
  .value-integrity { left: 342px; top: 470px; }
  .value-sincerity { left: 346px; top: 683px; }
  .value-humility { left: 346px; top: 921px; }
</style>
</head>
<body>
<main class="poster">
  <header class="masthead">
    <div class="brand"><span class="brand-dot"></span><span class="brand-name">The Mindwell Company</span></div>
  </header>

  <div class="backdrop backdrop-award" role="img" aria-label="Faint outline of an award rosette"></div>
  <div class="backdrop backdrop-scales" role="img" aria-label="Faint outline of justice scales"></div>
  <div class="backdrop backdrop-hearts" role="img" aria-label="Faint outline of two hearts"></div>
  <div class="backdrop backdrop-people" role="img" aria-label="Faint outline of two people standing together"></div>

  <div class="icon icon-award" role="img" aria-label="Award rosette with star icon"></div>
  <div class="icon icon-scales" role="img" aria-label="Balance scales icon"></div>
  <div class="icon icon-hearts" role="img" aria-label="Two hearts icon"></div>
  <div class="icon icon-people" role="img" aria-label="Two people side by side icon"></div>

  <section class="value value-excellence">
    <h2 class="value-title">Excellence</h2>
    <p class="value-text">We deliver quality services of unmatched value, constantly raising the bar on our performance, through <strong>a commitment to excellence, innovation, teamwork, ongoing learning, continuous improvement,</strong> an intense focus on client needs, and a dedication to meet those needs with a sense of urgency.</p>
  </section>

  <section class="value value-integrity">
    <h2 class="value-title">Integrity</h2>
    <p class="value-text">We demonstrate honesty, fairness, openness and clear boundaries in all our interactions, behaviours and practices within the organisation and with our clients, stakeholders and the wider community. We act in accordance with our values, even when it’s difficult. We adhere to the highest ethical standards as we strive to do what is right and fair for our clients and for each other.</p>
  </section>

  <section class="value value-sincerity">
    <h2 class="value-title">Sincerity</h2>
    <p class="value-text">We embrace human emotions and values, and believe that sincerity is a fundamental human behaviour. We are honest with our team, and with clients in the work we do, and the way we do it. We set high expectations for ourselves to motivate hard work, and we will offer clients something that has been crafted with care, consideration and with authenticity, without cutting corners. We will put people first, and will always genuinely care.</p>
  </section>

  <section class="value value-humility">
    <h2 class="value-title">Humility</h2>
    <p class="value-text">We believe in a flat hierarchy, and that every person within the organisation is a floor sweeper. We’re not always right — we don’t have all the answers — and we know it. We’re all humans after all, and we’re not afraid to ask for help. We encourage everyone to Be Yourself, Be Open, Stay Hungry and Humble, Collaborate, Challenge, Decide and Just Do.</p>
  </section>

  <footer class="footer">www.mindwellcompany.com.au</footer>
</main>
</body>
</html>
```